Webpage Design Layout for Thanksgiving/App Charity

Hi,

I am putting together a website called http://cloverbright.example with the intention of getting app developers to giveaway their usual thanksgiving discount to a charity rather than to the customer.

I am looking for a one page design (not coded) that will have;

1. A header and small description of the idea. For example;

"Cloverbright - Kindness That Counts"

Cloverbright is a movement that lets developers and users pass on the usual Thanksgiving discounts to people and communities who need it most. Buy your favourite apps from the links below and 40% of the price goes directly to charity"

2. A small section outlining the charity (not yet selected) with a link to learn more and a 'Play Video' button. I'd like to include a video of the charity.

3. A grid showing the available apps with an 'About' button and 'Buy Now' button

4. a FAQ underneath the apps

5. Some kind of prominent "Money raised" bar that will go near the top of the page

6. A footer section with contact info, mailing list sign up.

7. A countdown timer near the top that will countdown until the charity is over

8. A logo that would represent Apps + Thanksgiving

Obviously since this ties in with thanksgiving and apps I'd like to make it a fun turkey or thanksgiving themed page.

Please use Google Fonts and make sure to have the rights to any images used.

Target Market(s)

I want to appeal to every day phone and computer users. It should be a fun page but that also display credibility and confidence for purchasers/visitors.

Industry/Entity Type

Software

Number of Pages Required

1 page

Requirements
Must have
• Just a fun page that displays credibility and the importance of the idea

```html
<!DOCTYPE html>
<html lang="en">
<head>
<meta charset="utf-8">
<title>Cloverbright - Kindness That Counts</title>
<link rel="stylesheet" href="https://fonts.googleapis.com/css2?family=Open+Sans:wght@400;600;700;800&display=swap">
<style>
:root{
  --ink:#2b3440;
  --body:#3d4450;
  --muted:#5a606a;
  --gold:#f7b500;
  --green:#34a519;
  --green-dark:#2a8f12;
  --light:#f0f0f0;
  --white:#ffffff;
  --line:#d7d7d7;
}
*{box-sizing:border-box;margin:0;padding:0}
html,body{width:1200px;height:2493px;overflow:hidden}
body{font-family:"Open Sans",Arial,sans-serif;color:var(--body);background:var(--white);position:relative}

.site-header{position:absolute;top:0;left:0;width:1200px;height:96px;background:var(--white);display:flex;align-items:center;justify-content:space-between;padding:0 75px}
.brand{display:flex;align-items:center;gap:14px}
.brand-mark{width:50px;height:50px;border-radius:50%;background:var(--gold)}
.brand-text{display:flex;flex-direction:column;line-height:1}
.brand-name{font-size:36px;font-weight:800;color:var(--ink);letter-spacing:.5px}
.brand-tagline{font-size:17px;font-weight:600;color:var(--ink);margin-top:5px}
.main-nav{display:flex;gap:44px}
.main-nav a{font-size:13px;font-weight:700;color:var(--ink);text-decoration:none;letter-spacing:.5px}

.hero{position:absolute;top:96px;left:0;width:1200px;height:566px;overflow:hidden}
.hero-photo{position:absolute;inset:0;background:linear-gradient(100deg,#2d4548 0%,#3a5256 40%,#4a5e5f 70%,#6a7570 100%)}
.hero-shade{position:absolute;inset:0;background:rgba(20,35,38,.45)}
.hero-content{position:absolute;inset:0;text-align:center;color:var(--white)}
.hero-title{position:absolute;top:172px;left:0;width:100%;font-size:40px;font-weight:800;letter-spacing:.5px}
.hero-title .accent{color:var(--gold)}
.hero-sub{position:absolute;top:228px;left:0;width:100%;font-size:23px;font-weight:700}
.hero-lead{position:absolute;top:275px;left:170px;width:860px;font-size:17px;line-height:27px;font-weight:600}
.progress{position:absolute;top:414px;left:254px;width:692px;height:17px;background:var(--white);border-radius:9px;overflow:hidden}
.progress-fill{width:48%;height:100%;background:linear-gradient(#47b82a,var(--green-dark))}
.progress-labels{position:absolute;top:444px;left:254px;width:692px;display:flex;justify-content:space-between;font-size:16px;font-weight:700}
.countdown{position:absolute;top:495px;left:0;width:100%;display:flex;justify-content:center;align-items:center;gap:6px}
.countdown-unit{width:42px;height:42px;border:2px solid var(--white);color:var(--gold);font-size:24px;font-weight:700;display:flex;align-items:center;justify-content:center}
.countdown-sep{font-size:22px;font-weight:700;color:var(--white)}

.charity{position:absolute;top:662px;left:0;width:1200px;height:576px;background:var(--white);text-align:center}
.section-title{font-size:29px;font-weight:700;color:var(--ink)}
.charity .section-title{position:absolute;top:52px;width:100%}
.charity-lead{position:absolute;top:103px;width:100%;font-size:19px;font-weight:600;color:var(--muted)}
.charity-lead strong{color:var(--green);font-weight:700}
.video-frame{position:absolute;top:169px;left:264px;width:680px;height:344px;border:4px solid #c8c8c8;background:linear-gradient(120deg,#5a4a3a 0%,#7d6c55 35%,#3b4c5a 60%,#2a4c66 100%)}
.video-play{position:absolute;top:110px;left:309px;width:58px;height:58px;border-radius:50%;border:5px solid var(--white);background:rgba(0,0,0,.35);display:flex;align-items:center;justify-content:center}
.video-button{position:absolute;top:187px;left:244px;width:184px;height:46px;border-radius:23px;background:var(--green);color:var(--white);font-size:18px;font-weight:700;display:flex;align-items:center;justify-content:center}

.apps{position:absolute;top:1238px;left:0;width:1200px;height:657px;background:var(--light)}
.apps .section-title{position:absolute;top:48px;width:100%;text-align:center}
.app-card{position:absolute;width:512px;height:221px;background:var(--white);border-radius:12px}
.app-card:nth-of-type(1){top:120px;left:75px}
.app-card:nth-of-type(2){top:120px;left:615px}
.app-card:nth-of-type(3){top:371px;left:75px}
.app-card:nth-of-type(4){top:371px;left:615px}
.app-image{position:absolute;top:38px;left:23px;width:130px;height:135px;border-radius:8px;background:linear-gradient(135deg,#3b3f46 0%,#5b6a7a 40%,#e0643c 60%,#4fb0d8 80%,#f2c94c 100%)}
.app-name{position:absolute;top:24px;left:179px;font-size:21px;font-weight:700;color:var(--ink)}
.app-desc{position:absolute;top:58px;left:179px;width:300px;font-size:15px;line-height:24px;color:var(--body)}
.app-actions{position:absolute;top:146px;left:179px;display:flex;gap:12px}
.btn{width:140px;height:41px;border-radius:21px;color:var(--white);font-size:15px;font-weight:700;display:flex;align-items:center;justify-content:center}
.btn-learn{background:var(--gold)}
.btn-buy{background:var(--green)}

.faq{position:absolute;top:1895px;left:0;width:1200px;height:257px;background:var(--white)}
.faq .section-title{position:absolute;top:43px;width:100%;text-align:center}
.faq-item{position:absolute;top:112px;width:500px}
.faq-item:nth-of-type(1){left:76px}
.faq-item:nth-of-type(2){left:615px}
.faq-q{font-size:19px;font-weight:700;color:var(--ink)}
.faq-a{margin-top:8px;font-size:15px;line-height:24px;color:var(--body)}

.contact{position:absolute;top:2152px;left:0;width:1200px;height:341px;background:var(--light)}
.contact .section-title{position:absolute;top:40px;width:100%;text-align:center}
.contact-col{position:absolute;top:100px}
.contact-col.address{left:296px}
.contact-col.signup{left:617px}
.col-title{font-size:19px;font-weight:700;color:var(--ink)}
.contact-line{margin-top:10px;font-size:15px;color:var(--body);display:flex;align-items:center;gap:16px}
.contact-line:first-of-type{margin-top:12px}
.signup-form{position:absolute;top:161px;left:615px;width:332px;height:44px;background:var(--white);border:1px solid var(--line);border-radius:22px;display:flex;align-items:center;padding-left:20px;font-size:13px;color:var(--body)}
.signup-send{position:absolute;right:-1px;top:-1px;width:48px;height:44px;border-radius:0 22px 22px 0;background:var(--gold);display:flex;align-items:center;justify-content:center}
.footer-rule{position:absolute;top:246px;left:75px;width:1050px;height:1px;background:var(--line)}
.footer-bar{position:absolute;top:280px;left:75px;width:1050px;display:flex;justify-content:space-between;align-items:center}
.copyright{font-size:13px;color:var(--body)}
.social{display:flex;gap:22px}
.social span{width:18px;height:18px;border-radius:50%;background:#6d7178}
</style>
</head>
<body>

<header class="site-header">
  <div class="brand">
    <span class="brand-mark"></span>
    <div class="brand-text">
      <span class="brand-name">Cloverbright</span>
      <span class="brand-tagline">Kindness That Counts</span>
    </div>
  </div>
  <nav class="main-nav">
    <a href="#about">ABOUT</a>
    <a href="#charity-apps">CHARITY APPS</a>
    <a href="#faq">FAQ</a>
    <a href="#contact">CONTACT</a>
  </nav>
</header>

<section class="hero" id="about">
  <div class="hero-photo" role="img" aria-label="Hands holding a smartphone, surrounded by sketched app doodles"></div>
  <div class="hero-shade"></div>
  <div class="hero-content">
    <h1 class="hero-title">CLOVERBRIGHT: <span class="accent">GIVE WHERE IT MATTERS</span></h1>
    <p class="hero-sub">40% of all purchases goes to Charity</p>
    <p class="hero-lead">Cloverbright is a movement that lets developers and users pass on the usual Thanksgiving discounts to people and communities who need it most. Buy your favourite apps from the links below and 40% of the price goes directly to charity.</p>
    <div class="progress"><div class="progress-fill"></div></div>
    <div class="progress-labels"><span>Money Raised:&nbsp; $2349</span><span>Goal</span></div>
    <div class="countdown">
      <span class="countdown-unit">23</span><span class="countdown-sep">:</span>
      <span class="countdown-unit">03</span><span class="countdown-sep">:</span>
      <span class="countdown-unit">33</span>
    </div>
  </div>
</section>

<section class="charity" id="charity-apps">
  <h2 class="section-title">Charity Cloverbright</h2>
  <p class="charity-lead">Charity <strong>Cloverbright</strong> helps children develop the skills they need......</p>
  <div class="video-frame" role="img" aria-label="Video still: a hand tapping a donate button on a smartphone beside a notebook and coffee cup">
    <div class="video-play">
      <svg width="24" height="26" viewBox="0 0 24 26"><path d="M3 2 L22 13 L3 24 Z" fill="#ffffff"/></svg>
    </div>
    <div class="video-button">Play Video</div>
  </div>
</section>

<section class="apps">
  <h2 class="section-title">Available Apps</h2>
  <article class="app-card">
    <div class="app-image" role="img" aria-label="Phone with colourful app icons"></div>
    <h3 class="app-name">Lorem ipsum</h3>
    <p class="app-desc">SiteCraft is an easy to use website builder for desktop. The visual website builder is easy to use....</p>
    <div class="app-actions"><span class="btn btn-learn">Learn More</span><span class="btn btn-buy">Buy Now</span></div>
  </article>
  <article class="app-card">
    <div class="app-image" role="img" aria-label="Phone with colourful app icons"></div>
    <h3 class="app-name">Lorem ipsum</h3>
    <p class="app-desc">SiteCraft is an easy to use website builder for desktop. The visual website builder is easy to use....</p>
    <div class="app-actions"><span class="btn btn-learn">Learn More</span><span class="btn btn-buy">Buy Now</span></div>
  </article>
  <article class="app-card">
    <div class="app-image" role="img" aria-label="Phone with colourful app icons"></div>
    <h3 class="app-name">Lorem ipsum</h3>
    <p class="app-desc">SiteCraft is an easy to use website builder for desktop. The visual website builder is easy to use....</p>
    <div class="app-actions"><span class="btn btn-learn">Learn More</span><span class="btn btn-buy">Buy Now</span></div>
  </article>
  <article class="app-card">
    <div class="app-image" role="img" aria-label="Phone with colourful app icons"></div>
    <h3 class="app-name">Lorem ipsum</h3>
    <p class="app-desc">SiteCraft is an easy to use website builder for desktop. The visual website builder is easy to use....</p>
    <div class="app-actions"><span class="btn btn-learn">Learn More</span><span class="btn btn-buy">Buy Now</span></div>
  </article>
</section>

<section class="faq" id="faq">
  <h2 class="section-title">FAQ's</h2>
  <div class="faq-item">
    <h3 class="faq-q">How much money goes charity?</h3>
    <p class="faq-a">40% off all purchases that go through the Buy Now button for each app goes to charity.</p>
  </div>
  <div class="faq-item">
    <h3 class="faq-q">What Charity will the money go to?</h3>
    <p class="faq-a">40% off all purchases that go through the Buy Now button for each app goes to charity.</p>
  </div>
</section>

<footer class="contact" id="contact">
  <h2 class="section-title">Contact Us</h2>
  <div class="contact-col address">
    <h3 class="col-title">Address Info</h3>
    <p class="contact-line">42 Harvest Lane, Brookfield, BF1 7QT</p>
    <p class="contact-line">
      <svg width="12" height="12" viewBox="0 0 12 12"><path d="M2 1 L4.5 1 L5.5 3.5 L4 4.8 C4.8 6.5 5.5 7.2 7.2 8 L8.5 6.5 L11 7.5 L11 10 C11 10.6 10.6 11 10 11 C5 11 1 7 1 2 C1 1.4 1.4 1 2 1 Z" fill="#f7b500"/></svg>
      1-800-555-0142
    </p>
    <p class="contact-line">
      <svg width="12" height="10" viewBox="0 0 12 10"><rect x="0" y="0" width="12" height="10" rx="1" fill="#f7b500"/><path d="M0.5 1 L6 5.5 L11.5 1" stroke="#ffffff" stroke-width="1.2" fill="none"/></svg>
      hello@cloverbright.example
    </p>
  </div>
  <div class="contact-col signup">
    <h3 class="col-title">Email Sign Up</h3>
    <p class="contact-line">Vestibulum ante ipsum primis..</p>
  </div>
  <div class="signup-form">
    Enter Email Address
    <span class="signup-send">
      <svg width="18" height="18" viewBox="0 0 18 18"><path d="M1 8 L17 1 L12 17 L9 10 Z" fill="#ffffff"/></svg>
    </span>
  </div>
  <div class="footer-rule"></div>
  <div class="footer-bar">
    <p class="copyright">Copyright © 2017. Company Name. All Right Reserved</p>
    <div class="social" aria-label="Social links"><span></span><span></span><span></span><span></span><span></span></div>
  </div>
</footer>

</body>
</html>
```